Online training business needs new website

We need a new wordpress website as a result of a rebranding. The business is a crisis management training company focussed on online training and simulation exercises. We only need a 4 page site - home, about us, contact us and blog. However we must be able to add additional tabs in the header to redirect to our sales and marketing system (Velmora). As these change from time to time, we must be able to add and delete as required.The site must be editable by us, with a basic understanding of wordpress and no understanding of coding. We don't want to have to employ someone to change text, add posts or add a new workshops etc. The theme chosen must be easy to edit by a beginner.

Target Market(s)

Senior managers food and consumer goods companies

Industry/Entity Type

Consulting

Coding

Coded - Design and coding required

Font styles to use
Sans Serif

Requirements
Must have
• Home page, about us, contact us, blog
• Colour scheme from logo (attached) - maroon, blue and grey
• If you go to the current website "brightharbourgroup.com" and click on the "workshops" tab you will see the content I need on the home page for the stormpilotlabs.com site
Nice to have
• Modern, simple and minimalist design is preferred

```html
<!DOCTYPE html>
<html lang="en">
<head>
<meta charset="utf-8">
<title>Stormpilot Labs – Home</title>
<link rel="stylesheet" href="https://fonts.googleapis.com/css2?family=Roboto:ital,wght@0,300;0,400;0,500;0,700;1,300&display=swap">
<style>
  :root {
    --maroon: #8e1b4d;
    --blue: #0c4f8c;
    --grey: #efefef;
    --ink: #222222;
    --white: #ffffff;
    --hero-dark: #4a4d50;
    --hero-light: #a9aaa8;
  }
  * { box-sizing: border-box; margin: 0; padding: 0; }
  html, body { width: 1200px; height: 3273px; overflow: hidden; }
  body {
    position: relative;
    font-family: "Roboto", sans-serif;
    color: var(--ink);
    background: var(--white);
  }
  .abs { position: absolute; }

  /* Hero */
  .hero { left: 0; top: 0; width: 1200px; height: 738px; overflow: hidden; }
  .hero-photo {
    position: absolute; inset: 0;
    background: linear-gradient(125deg, var(--hero-light) 0%, #8d8f90 35%, #6e6f70 60%, var(--hero-dark) 100%);
  }
  .hero-shade { position: absolute; inset: 0; background: rgba(40, 40, 45, 0.35); }
  .brand-mark {
    position: absolute; left: 64px; top: 64px;
    display: flex; align-items: center; gap: 12px;
    color: var(--white); font-weight: 500; font-size: 34px; line-height: 1;
  }
  .brand-dot { width: 44px; height: 44px; border-radius: 50%; background: var(--white); flex: none; }
  .main-nav {
    position: absolute; top: 104px; right: 10px;
    display: flex; gap: 14px;
    color: var(--white); font-size: 28px; font-weight: 400;
  }
  .hero-title {
    position: absolute; top: 326px; width: 100%; text-align: center;
    color: var(--white); font-size: 48px; font-weight: 400;
  }
  .hero-tagline {
    position: absolute; top: 412px; left: 180px; width: 840px; text-align: center;
    color: var(--white); font-size: 35px; font-weight: 300; line-height: 45px;
  }
  .scroll-cue { position: absolute; left: 580px; top: 672px; }

  /* Mission band */
  .mission {
    left: 0; top: 738px; width: 1200px; height: 179px;
    background: var(--maroon); color: var(--white);
    display: flex; align-items: center; justify-content: center; text-align: center;
    font-size: 41px; font-weight: 400; line-height: 50px;
  }

  /* Intro */
  .intro-text { font-size: 28px; font-weight: 300; line-height: 35px; color: var(--ink); }
  .intro-left { left: 98px; top: 948px; width: 460px; }
  .intro-right { left: 657px; top: 948px; width: 470px; }
  .intro-right p + p { margin-top: 36px; }
  .intro-photo {
    left: 98px; top: 1159px; width: 447px; height: 281px;
    background: linear-gradient(135deg, #3b4650 0%, #8c96a0 50%, #d7d4cf 100%);
  }

  /* Next workshops */
  .workshops-band { left: 0; top: 1517px; width: 1200px; height: 432px; background: var(--maroon); color: var(--white); }
  .workshops-title { position: absolute; top: 38px; width: 100%; text-align: center; font-size: 36px; font-weight: 400; }
  .workshops-sub { position: absolute; top: 88px; width: 100%; text-align: center; font-size: 28px; font-weight: 300; }
  .event { position: absolute; top: 161px; width: 306px; text-align: center; }
  .event-photo { width: 306px; height: 186px; }
  .event-photo.sydney { background: linear-gradient(180deg, #bcd8ec 0%, #5f90a8 45%, #2f7c8c 100%); }
  .event-photo.melbourne { background: linear-gradient(180deg, #9fc3e3 0%, #8b9aa6 55%, #555d62 100%); }
  .event-caption { margin-top: 12px; font-size: 22px; font-weight: 400; }

  /* Offers */
  .offer { top: 2073px; width: 234px; height: 277px; }
  .offer-photo { width: 234px; height: 240px; }
  .offer-photo.workshops { background: linear-gradient(135deg, #5b4334 0%, #b7a89a 60%, #e7e3dd 100%); }
  .offer-photo.course { background: linear-gradient(135deg, #2a2a2c 0%, #6b6d70 55%, #bdbcb8 100%); }
  .offer-photo.simulations { background: linear-gradient(135deg, #d8d6d2 0%, #a08d7d 55%, #5a4f49 100%); }
  .offer-label {
    height: 37px; background: var(--blue); color: var(--white);
    font-size: 20px; line-height: 37px; text-align: center; text-transform: uppercase;
  }

  /* Why choose us */
  .why { left: 0; top: 2440px; width: 1200px; height: 314px; background: var(--grey); }
  .why-title { position: absolute; top: 40px; width: 100%; text-align: center; font-size: 37px; font-weight: 400; color: var(--ink); }
  .why-quote {
    position: absolute; left: 124px; top: 136px; width: 1000px;
    font-size: 30px; font-style: italic; font-weight: 300; line-height: 34px; color: var(--ink);
  }
  .why-arrow { position: absolute; top: 156px; }

  /* Partner row */
  .partner {
    top: 2840px; display: flex; align-items: center; gap: 10px;
    color: var(--maroon); font-size: 34px; font-weight: 500;
  }
  .partner-dot { width: 40px; height: 40px; border-radius: 50%; background: var(--maroon); flex: none; }

  /* Footer */
  .site-footer { left: 0; top: 2979px; width: 1200px; height: 294px; background: var(--blue); color: var(--white); }
  .footer-col { position: absolute; top: 60px; text-align: center; font-size: 28px; font-weight: 300; line-height: 37px; }
  .footer-col h3 { font-size: 30px; font-weight: 500; line-height: 37px; }
  .footer-map { position: absolute; left: 851px; top: 60px; font-size: 28px; font-weight: 300; color: #c8d6e6; }
  .social { position: absolute; left: 852px; top: 218px; display: flex; gap: 22px; }
  .social span { width: 38px; height: 38px; border-radius: 6px; background: var(--white); }
</style>
</head>
<body>

<header class="abs hero">
  <div class="hero-photo" role="img" aria-label="Overhead photo of a team working at a desk with laptops, tablets and documents"></div>
  <div class="hero-shade"></div>
  <div class="brand-mark"><span class="brand-dot"></span>Stormpilot Labs</div>
  <nav class="main-nav">
    <span>Home</span><span>About</span><span>Contact</span><span>Blog</span><span>Workshops</span><span>Online Course</span><span>Simulations</span>
  </nav>
  <h1 class="hero-title">Welcome to Stormpilot Labs</h1>
  <p class="hero-tagline">protect your brand | reconnect with customers | strengthen your business</p>
  <svg class="scroll-cue" width="40" height="28" viewBox="0 0 40 28" aria-hidden="true">
    <polyline points="5,6 20,21 35,6" fill="none" stroke="#ffffff" stroke-width="7" stroke-linecap="round" stroke-linejoin="round"/>
  </svg>
</header>

<section class="abs mission">
  <h2 style="font:inherit">Workshops &amp; simulations to help food and<br>consumer goods companies prevent a crisis</h2>
</section>

<p class="abs intro-text intro-left">If you are a food or consumer goods manufacturer, distributor or retailer, a major incident or a product recall can quickly escalate into a crisis!</p>
<div class="abs intro-photo" role="img" aria-label="Photo of two business people shaking hands across a desk"></div>
<div class="abs intro-text intro-right">
  <p>The average cost of a crisis is $10m and 25% cost over $100m</p>
  <p>Small and medium size businesses often don't survive at all</p>
  <p>The largest cost to any size business is to your reputation &amp; brand - that impacts customer relationships &amp; long term sales!</p>
  <p>Reputation risk remains the number one concern of senior executives, but most are unprepared for a crisis</p>
</div>

<section class="abs workshops-band">
  <h2 class="workshops-title">NEXT WORKSHOPS</h2>
  <p class="workshops-sub">Click to register</p>
  <div class="event" style="left:207px">
    <div class="event-photo sydney" role="img" aria-label="Photo of Sydney harbour and city skyline"></div>
    <p class="event-caption">Sydney, 28-29 March 2019</p>
  </div>
  <div class="event" style="left:668px">
    <div class="event-photo melbourne" role="img" aria-label="Photo of Melbourne skyline with a river bridge"></div>
    <p class="event-caption">Melbourne, 4-5 April, 2019</p>
  </div>
</section>

<div class="abs offer" style="left:120px">
  <div class="offer-photo workshops" role="img" aria-label="Photo of a workshop table with notes and coffee"></div>
  <div class="offer-label">Workshops</div>
</div>
<div class="abs offer" style="left:482px">
  <div class="offer-photo course" role="img" aria-label="Photo of hands typing on a laptop"></div>
  <div class="offer-label">Online Course</div>
</div>
<div class="abs offer" style="left:838px">
  <div class="offer-photo simulations" role="img" aria-label="Photo of a person using a phone beside a laptop and coffee"></div>
  <div class="offer-label">Simulations</div>
</div>

<section class="abs why">
  <h2 class="why-title">WHY CHOOSE US</h2>
  <svg class="why-arrow" style="left:38px" width="24" height="34" viewBox="0 0 24 34" aria-hidden="true">
    <polyline points="19,4 6,17 19,30" fill="none" stroke="#8e1b4d" stroke-width="6" stroke-linecap="round" stroke-linejoin="round"/>
  </svg>
  <p class="why-quote">"Lorem ipsum dolor sit amet, consectetur adipiscing elit. Etiam blandit mi sit amet mi tempus, in pretium lectus maximus. Morbi eget tempus nibh, in vestibulum odio. Aenean vitae ex porta ligula sodales vehicula et ut dolor."</p>
  <svg class="why-arrow" style="left:1090px" width="24" height="34" viewBox="0 0 24 34" aria-hidden="true">
    <polyline points="5,4 18,17 5,30" fill="none" stroke="#8e1b4d" stroke-width="6" stroke-linecap="round" stroke-linejoin="round"/>
  </svg>
</section>

<div class="abs partner" style="left:34px"><span class="partner-dot"></span>Stormpilot</div>
<div class="abs partner" style="left:352px"><span class="partner-dot"></span>Stormpilot</div>
<div class="abs partner" style="left:668px"><span class="partner-dot"></span>Stormpilot</div>
<div class="abs partner" style="left:982px"><span class="partner-dot"></span>Stormpilot</div>

<footer class="abs site-footer">
  <div class="footer-col" style="left:168px;width:200px">
    <h3>Contact</h3>
    <p>Tel. ********</p>
    <p>Email. ********</p>
  </div>
  <div class="footer-col" style="left:498px;width:200px">
    <h3>Find us</h3>
    <p>Address</p>
  </div>
  <p class="footer-map">MAP</p>
  <div class="social" aria-label="Social links"><span></span><span></span><span></span><span></span></div>
</footer>

</body>
</html>
```